Upsell Vertical Banner Ad Design For B2B Marketing Agency Vertical 768px × 1180px IS THE SIZE

I need a banner made for my website www.brightlanepromotionhub.biz This banner will be an upsell advertisement for after someone signs up for my monthly program. When they login to their account for the 1st time I will give them the chance to upgrade their account to our annual program with just one click.

this is a page that upsells it currently to give you an idea how we market ourselves:
https://tlpx.pagevault-example.com/page/tlp-annual-upsell

Use this content:

Are You Ready To Commit To Taking Your Business To The Next Level?

Because We're In This For The Long-Haul and Dedicated To Your Success...

Save $300 By Upgrading To An Annual Membership And Pay Only $74/mth

((BUTTON))Yes, Upgrade My Plan Right Now!

*Must prepay the full year at only $898/yr!

Target Market(s)

business owners

Industry/Entity Type

Marketing

Requirements
Must have
• 768px × 1180px IS THE SIZE vertical

Use this content:

Nice to have
• Use this content:

Should not have
• Use this content:

```html
<!DOCTYPE html>
<html lang="en">
<head>
<meta charset="utf-8">
<title>Bright Lane Promotion Hub – Annual Upgrade</title>
<link href="https://fonts.googleapis.com/css2?family=Poppins:wght@600&family=Josefin+Sans:wght@700&family=Carlito:wght@700&display=swap" rel="stylesheet">
<style>
  :root {
    --sky-top: #3b6ef7;
    --sky-mid: #1f4fd6;
    --sky-bottom: #0a2c93;
    --white: #ffffff;
    --ink-blue: #1748ad;
    --ribbon-light: #52d845;
    --ribbon-dark: #20a52b;
    --button-top: #fff400;
    --button-bottom: #ffc400;
    --button-text: #111111;
  }
  html, body {
    margin: 0;
    padding: 0;
    width: 781px;
    height: 1200px;
    overflow: hidden;
  }
  .banner {
    position: relative;
    width: 781px;
    height: 1200px;
    overflow: hidden;
    background: linear-gradient(180deg, var(--sky-top) 0%, var(--sky-mid) 55%, var(--sky-bottom) 100%);
    font-family: "Poppins", "Century Gothic", sans-serif;
    font-weight: 600;
    color: var(--white);
    text-align: center;
  }
  .brand {
    position: absolute;
    left: 26px;
    top: 30px;
    display: flex;
    align-items: center;
    gap: 8px;
    font-size: 15px;
    letter-spacing: 0.5px;
    text-transform: uppercase;
    color: var(--white);
  }
  .brand-mark {
    width: 18px;
    height: 18px;
    background: var(--white);
  }
  .headline {
    position: absolute;
    left: 0;
    right: 0;
    top: 120px;
    margin: 0;
    font-weight: 600;
    font-size: 44px;
    line-height: 52px;
  }
  .headline .second {
    display: block;
    font-size: 37px;
    line-height: 44px;
  }
  .highlight {
    position: absolute;
    left: 126px;
    top: 221px;
    width: 520px;
    height: 104px;
    background: var(--white);
    transform: rotate(-2deg);
    box-shadow: 0 4px 10px rgba(0, 20, 80, 0.35);
    display: flex;
    align-items: center;
    justify-content: center;
    font-family: "Josefin Sans", "Gill Sans", sans-serif;
    font-size: 70px;
    color: var(--ink-blue);
    padding-top: 10px;
    box-sizing: border-box;
    letter-spacing: 1px;
  }
  .promise {
    position: absolute;
    left: 0;
    right: 0;
    top: 428px;
    margin: 0;
    font-size: 38px;
    line-height: 51px;
  }
  .ribbon {
    position: absolute;
    left: 189px;
    top: 688px;
    width: 402px;
    height: 94px;
  }
  .ribbon-label {
    position: absolute;
    left: 189px;
    top: 688px;
    width: 402px;
    height: 94px;
    line-height: 94px;
    font-size: 62px;
    color: var(--white);
  }
  .offer {
    position: absolute;
    left: 0;
    right: 0;
    top: 790px;
    margin: 0;
    font-size: 39px;
    line-height: 51px;
  }
  .offer .price {
    display: block;
    font-size: 46px;
    line-height: 50px;
  }
  .cta {
    position: absolute;
    left: 119px;
    top: 1039px;
    width: 544px;
    height: 86px;
    background: linear-gradient(180deg, var(--button-top) 0%, var(--button-bottom) 100%);
    box-shadow: 0 0 22px rgba(255, 230, 60, 0.55);
    display: flex;
    align-items: center;
    justify-content: center;
    font-family: "Carlito", "Calibri", sans-serif;
    font-weight: 700;
    font-size: 33px;
    color: var(--button-text);
    text-decoration: none;
  }
  .fine-print {
    position: absolute;
    left: 0;
    right: 0;
    top: 1140px;
    margin: 0;
    font-family: "Poppins", "Century Gothic", sans-serif;
    font-weight: 400;
    font-size: 22px;
  }
</style>
</head>
<body>
  <section class="banner">
    <div class="brand"><span class="brand-mark"></span>Bright Lane Promotion Hub</div>

    <h1 class="headline">Are you ready to commit<span class="second">to taking your business to the</span></h1>
    <div class="highlight">NEXT LEVEL?</div>

    <p class="promise">Because we're in this for the<br>long-haul and dedicated to<br>your success...</p>

    <svg class="ribbon" viewBox="0 0 402 94" aria-hidden="true">
      <defs>
        <linearGradient id="ribbonFill" x1="0" y1="0" x2="0" y2="1">
          <stop offset="0" stop-color="var(--ribbon-light)"/>
          <stop offset="1" stop-color="var(--ribbon-dark)"/>
        </linearGradient>
      </defs>
      <path d="M0 2 Q201 14 402 2 L370 47 L402 92 Q201 80 0 92 L32 47 Z" fill="url(#ribbonFill)"/>
    </svg>
    <div class="ribbon-label">Save $300</div>

    <p class="offer">by upgrading to an annual<br>membership and pay only<span class="price">$74/mth</span></p>

    <a class="cta" href="https://tlpx.pagevault-example.com/page/tlp-annual-upsell">Yes, upgrade my plan right now!</a>

    <p class="fine-print">*Must prepay the full year at only $898/yr!</p>
  </section>
</body>
</html>
```